'Private English tutoring'

I need a flyer design to advertise private English tutoring. I am offering lessons to ethnic minority groups in my local area in south Belfast. The biggest ethnic minorities groups are Chinese, Polish and Indian and African. I can teach at any level, from beginner English to advanced. The tutoring will be either one on one or small groups of four students. I can teach adults and children but my preference would be to teach adults.

The flyer would need to be easily understood by people who have English as a second language.

I am also offering proof reading and editing services to students at local universities and colleges.

Target Market(s)

Adults of ethnic minorities who may not speak or read much English

Industry/Entity Type

Tutoring

Font styles to use
Serif

Requirements
Must have
• It needs to communicate that I am an accredited TEFL (Teaching English as a Foreign language) tutor with 2 years experience and that I tutor Beginners - Advanced students. It would also need to say that I offer proof reading and editing services. It would also need to communicate the cost of lessons are £15, but there are group rates for groups of 2-4 students. It would need to include my contact details which are as follows: contact Nora Calloway BTh at 07812639504 or email noracallowayenglish@vendrimail.com
Nice to have
• In terms of design I would like it to be warm and inviting and something which would convey an atmosphere of learning for non English speakers. Other than that I don't have any preferences.
Should not have
• Nothing which is going to be offensive to ethnic minorities.
• No pictures of people

```html
<!DOCTYPE html>
<html lang="en">
<head>
<meta charset="utf-8">
<title>Private English Tutoring Flyer</title>
<link rel="stylesheet" href="https://fonts.googleapis.com/css2?family=Oswald:wght@600;700&family=Playfair+Display:ital,wght@1,600&family=Roboto+Condensed:wght@400;700&display=swap">
<style>
  :root {
    --page-bg: #e9e6e1;
    --paper: #ffffff;
    --headline-red: #e0402d;
    --orange: #ea5a2a;
    --orange-deep: #d9481f;
    --sky: #3cc0ef;
    --sky-light: #8fd7f3;
    --ocean: #2a98c4;
    --pale-blue: #a3dcf3;
    --navy: #1b3a52;
    --cream: #f4ed9e;
    --white: #ffffff;
    --letter-green: #9ccb2e;
    --letter-blue: #8ec6ea;
    --letter-red: #e8432f;
    --letter-yellow: #f3e21c;
    --letter-pink: #c27cc0;
    --letter-purple: #8a84c6;
  }
  * { box-sizing: border-box; margin: 0; padding: 0; }
  html, body { width: 1200px; height: 1000px; overflow: hidden; }
  body { background: var(--page-bg); position: relative; font-family: "Roboto Condensed", Arial, sans-serif; }

  .flyer {
    position: absolute; left: 285px; top: 57px;
    width: 630px; height: 886px;
    background: var(--paper);
    overflow: hidden;
    box-shadow: 0 4px 18px rgba(0,0,0,.18);
  }
  .abs { position: absolute; left: 0; width: 100%; text-align: center; }

  .headline {
    top: 20px; font-family: "Oswald", Impact, sans-serif; font-weight: 700;
    font-size: 50px; line-height: 62px; color: var(--headline-red); letter-spacing: .5px;
  }
  .headline .joiner { font-family: "Playfair Display", Georgia, serif; font-style: italic; font-weight: 600; font-size: 40px; }

  .hero-photo {
    top: 210px; height: 200px;
    background: linear-gradient(180deg, #ffffff 0%, #f6ece3 40%, #efd9c8 75%, #f3e2d4 100%);
  }

  .subject-word {
    top: 68px; padding-left: 20px;
    font-family: "Roboto Condensed", Arial, sans-serif; font-weight: 700;
    font-size: 180px; line-height: 180px; letter-spacing: -8px;
  }
  .subject-word .l1 { color: var(--letter-green); }
  .subject-word .l2 { color: var(--letter-blue); }
  .subject-word .l3 { color: var(--letter-red); }
  .subject-word .l4 { color: var(--letter-yellow); }
  .subject-word .l5 { color: var(--letter-pink); }
  .subject-word .l6 { color: var(--letter-purple); }
  .subject-word .l7 { color: var(--letter-blue); }

  .band-sky-edge { top: 408px; height: 10px; background: var(--sky-light); }
  .band-sky { top: 418px; height: 228px; background: var(--sky); }
  .band-ocean { top: 646px; height: 177px; background: var(--ocean); }
  .band-pale { top: 823px; height: 63px; background: var(--pale-blue); }

  .option-ring {
    position: absolute; top: 308px; width: 240px; height: 240px; border-radius: 50%;
    background: linear-gradient(180deg, #f7f7f7, #dcdcdc);
    box-shadow: 0 6px 14px rgba(0,0,0,.18);
  }
  .option-ring.left { left: 30px; }
  .option-ring.right { left: 350px; }
  .option-disc {
    position: absolute; left: 17px; top: 17px; width: 206px; height: 206px; border-radius: 50%;
    background: radial-gradient(circle at 40% 30%, var(--orange), var(--orange-deep));
  }
  .option-icon {
    position: absolute; top: 28px; height: 68px; border-radius: 8px;
    background: rgba(255,255,255,.18);
  }
  .left .option-icon { left: 63px; width: 80px; }
  .right .option-icon { left: 38px; width: 130px; }
  .option-label {
    position: absolute; left: 0; width: 100%; top: 112px; text-align: center;
    color: var(--white); font-weight: 700; font-size: 28px; line-height: 33px;
  }
  .option-note { display: block; font-size: 12px; line-height: 16px; font-weight: 400; }

  .or-badge {
    position: absolute; left: 270px; top: 381px; width: 90px; height: 90px; border-radius: 50%;
    background: var(--white); box-shadow: 0 3px 8px rgba(0,0,0,.15);
  }
  .or-badge span {
    position: absolute; left: 10px; top: 10px; width: 70px; height: 70px; border-radius: 50%;
    background: var(--orange); color: var(--white); font-weight: 700; font-size: 32px;
    line-height: 64px; text-align: center;
  }

  .price { top: 578px; color: var(--white); font-weight: 700; font-size: 36px; line-height: 40px; }
  .price-note { top: 615px; color: var(--white); font-weight: 700; font-size: 18px; line-height: 22px; }

  .tutor-name { top: 670px; color: var(--cream); font-weight: 700; font-size: 38px; line-height: 46px; }
  .tutor-phone { top: 719px; color: var(--white); font-weight: 700; font-size: 40px; line-height: 48px; }
  .tutor-phone svg { width: 26px; height: 26px; vertical-align: 2px; margin-right: 10px; }
  .tutor-email { top: 772px; color: var(--white); font-size: 24px; line-height: 30px; }
  .tutor-email .at { color: var(--cream); font-weight: 700; margin-right: 10px; }

  .credential { top: 835px; color: var(--navy); font-weight: 700; font-size: 20px; line-height: 24px; letter-spacing: .3px; }
  .services { top: 860px; color: var(--navy); font-size: 14px; line-height: 18px; }
</style>
</head>
<body>
  <main class="flyer">
    <h1 class="abs headline">BEGINNER <span class="joiner">to</span> ADVANCED</h1>

    <div class="abs hero-photo" role="img" aria-label="Photo of raised hands holding up large colourful letters"></div>

    <h2 class="abs subject-word"><span class="l1">E</span><span class="l2">n</span><span class="l3">g</span><span class="l4">l</span><span class="l5">i</span><span class="l6">s</span><span class="l7">h</span></h2>

    <div class="abs band-sky-edge"></div>
    <div class="abs band-sky"></div>
    <div class="abs band-ocean"></div>
    <div class="abs band-pale"></div>

    <div class="option-ring left">
      <div class="option-disc">
        <div class="option-icon" role="img" aria-label="Icon of a single student at a desk"></div>
        <p class="option-label">ONE-TO-ONE<br>LESSONS</p>
      </div>
    </div>

    <div class="or-badge"><span>or</span></div>

    <div class="option-ring right">
      <div class="option-disc">
        <div class="option-icon" role="img" aria-label="Icon of a small group of students at a table"></div>
        <p class="option-label">SMALL<br>GROUPS<span class="option-note">(UP TO 4 STUDENTS)</span></p>
      </div>
    </div>

    <p class="abs price">£15 per lesson</p>
    <p class="abs price-note">Contact me for group rates</p>

    <p class="abs tutor-name">Nora Calloway BTh</p>
    <p class="abs tutor-phone"><svg viewBox="0 0 24 24" aria-hidden="true"><path fill="#f4ed9e" d="M3 8c0-2 2-4 9-4s9 2 9 4v2h-5V8.5c-1-.6-7-.6-8 0V10H3V8zm4 3h10l3 8H4l3-8zm5 2a2.5 2.5 0 1 0 0 5 2.5 2.5 0 0 0 0-5z"/></svg>078 1263 9504</p>
    <p class="abs tutor-email"><span class="at">@</span>noracallowayenglish@vendrimail.com</p>

    <p class="abs credential">ACCREDITED TEFL TUTOR WITH 2 YEARS EXPERIENCE</p>
    <p class="abs services">Proof reading and editing services to students at local universities and colleges</p>
  </main>
</body>
</html>
```